New Company Business Card Design

I have a new company logo and I want a new business card design. I dont know if the logo file i attached is in the correct format or quality. We are a New York City Specialty construction Firm specializing in high risk out of the box projects. I want a simple and classy business card that people will his card is as crisp as the work his company does.

Target Market(s)

Clients in the heavy construction industry in New York City

Industry/Entity Type

Construction Company

Contact Information for Business Card

Simple Classy - DIFFERENT

Font styles to use
Other font styles liked:
• Mach the logo font in some way

Colors

Designer to choose colors to be used in the design.

Requirements
Must have
• Uniqueness
Nice to have
• Nothing particular - Just different and classy - Timeless
Should not have
• Goofy Shit or Gimmicky shit

```html
<!DOCTYPE html>
<html lang="en">
<head>
<meta charset="utf-8">
<title>Korvel Builders – Business Card</title>
<link rel="stylesheet" href="https://fonts.googleapis.com/css2?family=Open+Sans:wght@400;600;700;800&display=swap">
<style>
  :root {
    --backdrop: #262626;
    --card-white: #ffffff;
    --brand-blue: #1f3f73;
    --brand-blue-deep: #1a3766;
    --back-blue: #2c4c82;
    --ink: #3a3a3a;
    --ink-soft: #555555;
    --on-blue: #ffffff;
  }
  * { margin: 0; padding: 0; box-sizing: border-box; }
  html, body {
    width: 1200px; height: 900px; overflow: hidden;
    background: var(--backdrop);
    font-family: "Open Sans", Arial, sans-serif;
  }
  .canvas { position: relative; width: 1200px; height: 900px; }

  .card {
    position: absolute;
    width: 525px; height: 300px;
    border-radius: 3px;
    box-shadow: 0 10px 30px rgba(0,0,0,0.45);
  }

  /* Front side */
  .card-front {
    left: 70px; top: 420px;
    background: var(--card-white);
    border-left: 6px solid var(--brand-blue);
  }
  .holder { position: absolute; left: 32px; top: 30px; }
  .holder-name {
    font-size: 17px; font-weight: 700; letter-spacing: 0.5px;
    color: var(--brand-blue); text-transform: uppercase;
  }
  .holder-title {
    font-size: 9px; font-weight: 600; letter-spacing: 0.6px;
    color: var(--ink-soft); text-transform: uppercase; margin-top: 2px;
  }
  .contact-list { position: absolute; left: 32px; top: 100px; list-style: none; }
  .contact-item {
    display: flex; align-items: flex-start; gap: 10px;
    margin-bottom: 9px; font-size: 12px; line-height: 15px; color: var(--ink);
  }
  .contact-icon {
    flex: none; width: 16px; height: 16px; border-radius: 3px;
    background: var(--brand-blue);
    display: flex; align-items: center; justify-content: center;
  }
  .contact-icon svg { width: 10px; height: 10px; }

  .wordmark {
    font-weight: 800; text-transform: uppercase; line-height: 1;
    letter-spacing: 0.5px;
  }
  .front-wordmark {
    position: absolute; right: 40px; top: 118px;
    color: var(--brand-blue); font-size: 26px; text-align: right;
  }
  .front-wordmark span { display: block; }
  .front-wordmark .wordmark-sub { font-size: 26px; }

  .office-address {
    position: absolute; right: 40px; bottom: 26px;
    text-align: right; font-size: 13px; line-height: 18px; color: var(--ink);
    font-style: normal;
  }

  /* Back side */
  .card-back {
    left: 610px; top: 120px;
    background: var(--back-blue);
    border-bottom: 6px solid var(--brand-blue-deep);
  }
  .back-wordmark {
    position: absolute; left: 0; right: 0; top: 98px;
    color: var(--on-blue); font-size: 32px; text-align: center;
  }
  .back-wordmark span { display: block; }
  .back-wordmark .wordmark-sub { font-size: 22px; margin-top: 6px; letter-spacing: 2px; }
  .back-url {
    position: absolute; left: 0; right: 0; top: 210px;
    text-align: center; font-size: 12px; color: var(--on-blue); opacity: 0.9;
  }
</style>
</head>
<body>
<main class="canvas">

  <section class="card card-back" aria-label="Card back">
    <div class="wordmark back-wordmark">
      <span>Korvel</span>
      <span class="wordmark-sub">Builders, Inc.</span>
    </div>
    <p class="back-url">https://korvel.com</p>
  </section>

  <section class="card card-front" aria-label="Card front">
    <div class="holder">
      <p class="holder-name">Alex Rowan</p>
      <p class="holder-title">Manager</p>
    </div>

    <ul class="contact-list">
      <li class="contact-item">
        <span class="contact-icon">
          <svg viewBox="0 0 24 24"><path fill="#fff" d="M6.6 10.8a15.1 15.1 0 0 0 6.6 6.6l2.2-2.2c.3-.3.7-.4 1-.2 1.1.4 2.3.6 3.6.6.6 0 1 .4 1 1V20c0 .6-.4 1-1 1A17 17 0 0 1 3 4c0-.6.4-1 1-1h3.5c.6 0 1 .4 1 1 0 1.3.2 2.5.6 3.6.1.3 0 .7-.2 1z"/></svg>
        </span>
        <span>555-014-2281<br>555-019-3307</span>
      </li>
      <li class="contact-item">
        <span class="contact-icon">
          <svg viewBox="0 0 24 24"><path fill="none" stroke="#fff" stroke-width="2.4" d="M3 6h18v12H3z M3 6l9 7 9-7"/></svg>
        </span>
        <span>alex@korvel.com</span>
      </li>
      <li class="contact-item">
        <span class="contact-icon">
          <svg viewBox="0 0 24 24"><g fill="none" stroke="#fff" stroke-width="2.2"><circle cx="12" cy="12" r="9"/><path d="M3 12h18M12 3c3 3 3 15 0 18M12 3c-3 3-3 15 0 18"/></g></svg>
        </span>
        <span>korvel.com</span>
      </li>
    </ul>

    <div class="wordmark front-wordmark">
      <span>Korvel</span>
      <span class="wordmark-sub">Builders, Inc.</span>
    </div>

    <address class="office-address">
      Marcus T. Hale<br>
      48 Harbor Line Avenue<br>
      Brookfield, New Jersey 07000
    </address>
  </section>

</main>
</body>
</html>
```